Happy Birthday Cards (from Law Firm)

Need classy, professional AND polished Happy Birthday Cards from law firm.

Please tie in the firm logo and colors somewhere with the picture on front or inside(but not used too many times)

Include company logo somewhere on the card, firm name (Morvena Brask Law, PLLC) www.morvenabrasklaw.example
Updates

Project Deadline Extended
Reason: Thank you for your patience. Had a family emergency.

Target Market(s)

Law firm clients ages 30 - 99

Industry/Entity Type

Law Firm

Font styles to use
Serif
Sans Serif
Decorative
Script

Requirements
Must have
• Must be classy, elegant, professional, polished from a business
• Birthday wish or message - you suggest one.
• For example "Enjoy every moment of your life. May everyday bring something new and exciting for you. May your birthday be as amazing as you."
Nice to have
• Would like several birthday card templates (for male/for female); traditional/fun

```html
<!DOCTYPE html>
<html lang="en">
<head>
<meta charset="utf-8">
<title>Birthday Card – Morvena Brask Law, PLLC</title>
<link href="https://fonts.googleapis.com/css2?family=Cinzel:wght@500&family=PT+Serif:wght@700&family=Oswald:wght@500&family=Great+Vibes&display=swap" rel="stylesheet">
<style>
  :root {
    --backdrop: #2c2c2e;
    --card: #ffffff;
    --card-tint: #eef4f8;
    --navy: #1d5673;
    --teal: #1f7f95;
    --rule: #7fa3b6;
    --gift-light: #a9dcee;
    --gift-deep: #3f86c2;
  }
  * { margin: 0; padding: 0; box-sizing: border-box; }
  html, body {
    width: 1200px; height: 900px; overflow: hidden;
    background: var(--backdrop);
  }
  .canvas { position: relative; width: 1200px; height: 900px; }

  .card {
    position: absolute;
    width: 700px; height: 400px;
    background: var(--card);
    box-shadow: 0 18px 40px rgba(0,0,0,.45);
    overflow: hidden;
  }

  /* Front */
  .card--front { left: 70px; top: 50px; }
  .greeting {
    position: absolute; left: 40px; top: 70px;
    width: 400px;
    font-family: "Great Vibes", cursive;
    font-weight: 400;
    color: var(--teal);
    line-height: .9;
  }
  .greeting__word { display: block; font-size: 118px; }
  .greeting__word--first { padding-left: 70px; }
  .greeting__word--second { padding-left: 40px; }

  .firm-mark {
    position: absolute; left: 455px; top: 150px;
    display: flex; align-items: center; gap: 12px;
  }
  .firm-mark__dot {
    width: 46px; height: 46px; border-radius: 50%;
    background: var(--navy);
    flex: none;
  }
  .firm-mark__name {
    font-family: "Cinzel", serif; font-weight: 500;
    font-size: 17px; line-height: 1.35; letter-spacing: 1px;
    color: var(--navy);
    border-top: 1px solid var(--rule);
    border-bottom: 1px solid var(--rule);
    padding: 4px 0;
  }

  /* Back */
  .card--back {
    left: 430px; top: 470px;
    background: linear-gradient(160deg, var(--card) 0%, var(--card) 45%, var(--card-tint) 100%);
  }
  .band { position: absolute; height: 14px; background: var(--navy); }
  .band--top { right: 0; top: 120px; width: 250px; }
  .band--bottom { left: 0; top: 262px; width: 250px; }
  .message {
    position: absolute; left: 170px; top: 140px; width: 500px;
    text-align: center; color: var(--navy);
  }
  .message__title {
    font-family: "Oswald", sans-serif; font-weight: 500;
    font-size: 20px; letter-spacing: 6px; text-transform: uppercase;
    margin-bottom: 6px;
  }
  .message__line {
    font-family: "PT Serif", serif; font-weight: 700;
    font-size: 17px; line-height: 1.35;
  }
  .back__photo {
    position: absolute; left: 0; bottom: 0;
    width: 300px; height: 124px;
    background: linear-gradient(90deg, var(--gift-light) 0%, var(--gift-deep) 50%, var(--card-tint) 100%);
  }
</style>
</head>
<body>
<main class="canvas">
  <section class="card card--front" aria-label="Card front">
    <h1 class="greeting">
      <span class="greeting__word greeting__word--first">Happy</span>
      <span class="greeting__word greeting__word--second">Birthday</span>
    </h1>
    <div class="firm-mark">
      <span class="firm-mark__dot"></span>
      <span class="firm-mark__name">Morvena Brask<br>Law, PLLC</span>
    </div>
  </section>

  <section class="card card--back" aria-label="Card back">
    <div class="band band--top"></div>
    <div class="message">
      <h2 class="message__title">Enjoy every moment of your life</h2>
      <p class="message__line">May everyday bring something new and exciting for you.</p>
      <p class="message__line">May your birthday be as amazing as you.</p>
    </div>
    <div class="band band--bottom"></div>
    <div class="back__photo" role="img" aria-label="Photo of a blue gift box with navy polka-dot ribbon beside a frosted cupcake with a candle"></div>
  </section>
</main>
</body>
</html>
```